Exciting new website for concierge aesthetic company

Simple, elegant, fresh design for female owned concierge aesthetic company, catering to both men and women ages 30-60. We would like a home page with an exciting catch phrase, a brief description of the company and a section to fill out an appointment request that includes a section for a referral. Please also have a book appointment link in the header of all pages that will link back to booking information form on home page. Separate pages to include:
- Services = 3 different services. Each service stating the name of the service and then providing a brief description. 3 services are "Private Session" for 1 client, "Group Session" for 2-5 clients, "Party" for 6+ clients. Will provide service descriptions text later. Item at bottom of page to allow description of how to "Host a Party".
- Products = 4 different product lines. Will provide pictures of product, brief description and link to manufacturer's website.
- Stories = brief client reviews to include before and after photos
- About us = Personal picture with brief description of owner's fun, exciting and family focussed lifestyle.
*Our domain is registered with parvox and we be using parvox for website hosting.

Target Market(s)

30-60 year old men and women, but mostly women

Industry/Entity Type

beauty and aesthetics

Coding

Coded - Design and coding required

Number of Pages Required

5+ page

Font styles to use
Sans Serif
Script

Colors
59FF00
82FF00
B8FF75
E3FFCB
F4FFEA
FFC000
F8CF3A
FAE287
FDF2CF
FEFAEE
F0912C
F2A743
F7CA91
FBE8D2
FDF5EE
E54698
E96AAD
F1A4CE
F9D9EA
FCEFF6

Requirements
Must have
• coded for parvox
Should not have
• corny pictures. No needles in pictures or graphics. No medical office or medical chair in pictures.

```html
<!DOCTYPE html>
<html lang="en">
<head>
<meta charset="utf-8">
<title>Glow Muse Concierge Aesthetics</title>
<link href="https://fonts.googleapis.com/css2?family=Playfair+Display:wght@400;700;900&display=swap" rel="stylesheet">
<style>
:root{
  --ink:#000;
  --text:#333;
  --muted:#6b6b6b;
  --white:#fff;
  --blush:#e9d3cf;
  --lilac:#bdbccb;
  --grey-panel:#e7e7e7;
  --field-line:#c9c9c9;
  --ghost:#e4e4e4;
}
*{margin:0;padding:0;box-sizing:border-box}
html,body{width:1200px;height:4097px;overflow:hidden}
body{position:relative;background:var(--white);font-family:"Playfair Display",serif;color:var(--text)}
.abs{position:absolute}
.band{position:absolute;left:0;width:1200px}
.gradient{background:linear-gradient(180deg,var(--blush) 0%,var(--lilac) 100%)}
.btn{position:absolute;background:var(--ink);color:var(--white);font-weight:700;font-size:11.5px;letter-spacing:.3px;display:flex;align-items:center;justify-content:center;text-transform:uppercase}
.photo{position:absolute}
h1,h2,h3{font-family:"Playfair Display",serif;color:var(--ink);font-weight:700}
.para{font-size:12.5px;line-height:21px;color:var(--text)}
.ghost-word{position:absolute;font-size:98px;color:var(--ghost);letter-spacing:2px;white-space:nowrap;transform-origin:left top;line-height:1}

.brand{position:absolute;left:212px;top:34px;display:flex;align-items:center;gap:10px}
.brand-mark{width:40px;height:40px;border:1.5px solid var(--ink);border-radius:50%}
.brand-name{font-size:27px;color:var(--ink);font-weight:400;line-height:1}
.brand-sub{font-size:7px;letter-spacing:3px;color:var(--ink);margin-top:4px}
.nav a{position:absolute;top:46px;font-size:11.5px;color:var(--muted);text-decoration:none}
.nav .active{color:var(--ink);border-bottom:1.5px solid var(--ink);padding-bottom:4px}

.service-card{position:absolute;width:382px;height:208px;color:var(--white)}
.service-title{position:absolute;left:27px;top:30px;font-size:25px;line-height:25px;font-weight:700}
.service-note{position:absolute;left:27px;top:104px;font-size:13px}
.service-more{position:absolute;left:27px;top:165px;font-size:12px;font-weight:700}
.service-more span{display:inline-block;width:44px;height:1px;background:var(--white);vertical-align:middle;margin-left:10px}

.product-card{position:absolute;top:2249px;width:188px;height:170px}
.product-card .frame{position:absolute;inset:10px;border:1px solid #777}
.product-card .shot{position:absolute;inset:11px;background:linear-gradient(180deg,#ecdcd8,#d6d2dc)}

.quote-box{position:absolute;background:var(--ink);color:var(--white);text-align:center;display:flex;flex-direction:column;align-items:center}
.field{position:absolute;height:30px;border:1px solid var(--field-line);background:var(--white);font-size:10px;color:#999;padding:9px 16px}
.footer-col{position:absolute;text-align:center;color:var(--white)}
.footer-col h4{font-size:13px;font-weight:700;letter-spacing:.5px;margin-bottom:10px}
.footer-col p{font-size:12px;line-height:22px;color:#ddd}
.social{position:absolute;top:3978px;width:26px;height:26px;border-radius:50%;background:var(--white)}
.divider{position:absolute;top:3860px;width:1px;height:68px;background:#bbb}
</style>
</head>
<body>

<!-- HERO -->
<section class="band gradient" style="top:0;height:656px"></section>
<header>
  <div class="brand">
    <span class="brand-mark"></span>
    <div><div class="brand-name">Glow Muse</div><div class="brand-sub">CONCIERGE AESTHETICS</div></div>
  </div>
  <nav class="nav">
    <a class="active" style="left:484px">HOME</a>
    <a style="left:552px">ABOUT US</a>
    <a style="left:643px">PRODUCT</a>
    <a style="left:734px">STORIES</a>
  </nav>
  <div class="btn" style="left:828px;top:32px;width:162px;height:43px">Book Appointment</div>
</header>
<div class="photo" role="img" aria-label="Portrait of a woman with eyes closed and a purple flower, set in an arch" style="left:629px;top:100px;width:390px;height:556px;border-radius:195px 195px 0 0;background:linear-gradient(180deg,#cdb0ad 0%,#d9bcb0 55%,#c2b0b9 100%)"></div>
<div class="abs" style="left:212px;top:221px;font-size:13px;letter-spacing:4.5px;color:var(--ink)">GLOW MUSE CONCIERGE AESTHETICS</div>
<h1 class="abs" style="left:210px;top:246px;font-size:76px;line-height:84px;font-weight:900;white-space:nowrap">BEAUTY &amp;<br>GLOW</h1>
<p class="abs para" style="left:212px;top:424px;width:360px;font-size:12px">Lorem ipsum dolor sit amet, consectetur adipiscing elit, sed do eiusmod tempor incididunt ut labore et dolore magna aliqua.</p>
<div class="btn" style="left:212px;top:486px;width:134px;height:40px">Get Started</div>

<!-- ABOUT -->
<div class="photo" role="img" aria-label="Smiling woman with long wavy hair" style="left:51px;top:627px;width:449px;height:623px;background:linear-gradient(180deg,#a08d76,#7d6a57)"></div>
<div class="ghost-word" style="left:1138px;top:660px;transform:rotate(90deg)">ABOUT US</div>
<h2 class="abs" style="left:587px;top:712px;font-size:34px">ABOUT US</h2>
<p class="abs para" style="left:587px;top:770px;width:400px;text-align:justify">Sed ut perspiciatis unde omnis iste natus error sit voluptatem accusantium doloremque laudantium, totam rem aperiam, eaque ipsa quae ab illo inventore veritatis et quasi architecto beatae vitae dicta sunt explicabo. Nemo enim ipsam voluptatem quia voluptas sit aspernatur aut odit aut fugit, sed quia consequuntur magni dolores eos qui ratione voluptatem sequi nesciunt. Neque porro quisquam est, qui dolorem ipsum quia dolor sit amet, consectetur, adipisci velit,</p>
<p class="abs para" style="left:587px;top:942px;width:400px;text-align:justify">sed quia non numquam eius modi tempora incidunt ut labore et dolore magnam aliquam quaerat voluptatem. Ut enim ad minima veniam quis nostrum exercitationem ullam corporis suscipit laboriosam,</p>
<div class="btn" style="left:587px;top:1025px;width:136px;height:41px">Learn More</div>
<div class="photo" role="img" aria-label="Man with facial treatment markings" style="left:401px;top:1144px;width:345px;height:223px;background:linear-gradient(135deg,#c9c6d2,#b49a88)"></div>
<div class="photo" role="img" aria-label="Woman with clear skin resting her face on her hand" style="left:783px;top:1144px;width:347px;height:223px;background:linear-gradient(135deg,#b49582,#d7bfb2)"></div>

<!-- SERVICES -->
<section class="band gradient" style="top:1440px;height:565px"></section>
<h2 class="abs" style="left:210px;top:1512px;font-size:34px;line-height:40px">OUR CORE<br>SERVICES</h2>
<p class="abs para" style="left:212px;top:1602px;width:290px;font-size:12px">Sed ut perspiciatis unde omnis iste natus error sit voluptatem accusantium doloremque laudantium.</p>
<div class="btn" style="left:212px;top:1666px;width:134px;height:40px">Learn More</div>

<div class="service-card" role="img" aria-label="Woman touching her face, private session" style="left:606px;top:1507px;height:209px;background:linear-gradient(90deg,#44505d,#6b6e77)">
  <div class="service-title">Private<br>Session</div>
  <div class="service-note">“Private Session” for 1 client.</div>
  <div class="service-more">MORE <span></span></div>
</div>
<div class="service-card" role="img" aria-label="Group of women smiling together, group session" style="left:210px;top:1730px;background:linear-gradient(90deg,#4a3b30,#6e5848)">
  <div class="service-title">Group<br>Session</div>
  <div class="service-note">“Group Session” for 2-5 clients</div>
  <div class="service-more">MORE <span></span></div>
</div>
<div class="service-card" role="img" aria-label="Group of diverse women posing, party" style="left:606px;top:1730px;background:linear-gradient(90deg,#5d4c45,#7a6458)">
  <div class="service-title">Party</div>
  <div class="service-note">“Party” for 6+ clients</div>
  <div class="service-more">MORE <span></span></div>
</div>

<!-- PRODUCTS -->
<div class="ghost-word" style="left:72px;top:2554px;transform:rotate(-90deg);font-size:92px">PRODUCTS</div>
<h2 class="abs" style="left:0;width:1200px;top:2062px;text-align:center;font-size:34px">OUR VALUE PRODUCTS</h2>
<p class="abs para" style="left:420px;width:360px;top:2120px;text-align:center;font-size:12px">Sed ut perspiciatis unde omnis iste natus error sit voluptatem accusantium doloremque laudantium.</p>

<div class="product-card gradient" style="left:205px"><div class="shot" role="img" aria-label="Skincare bottle with coral cap"></div><div class="frame"></div></div>
<div class="product-card gradient" style="left:406px"><div class="shot" role="img" aria-label="Slim skincare tube with coral cap"></div><div class="frame"></div></div>
<div class="product-card gradient" style="left:608px;width:187px"><div class="shot" role="img" aria-label="Pump bottle lotion"></div><div class="frame"></div></div>
<div class="product-card gradient" style="left:808px;width:187px"><div class="shot" role="img" aria-label="Cream jar with coral lid"></div><div class="frame"></div></div>
<div class="btn" style="left:533px;top:2460px;width:135px;height:42px">View All</div>

<!-- STORIES -->
<section class="band gradient" style="top:2570px;height:745px"></section>
<h2 class="abs" style="left:0;width:1200px;top:2630px;text-align:center;font-size:34px">OUR INTRESTING STORIES</h2>
<p class="abs para" style="left:390px;width:420px;top:2688px;text-align:center;font-size:12px">Sed ut perspiciatis unde omnis iste natus error sit voluptatem accusantium doloremque laudantium,</p>

<div class="photo" role="img" aria-label="Woman with colourful eye makeup" style="left:210px;top:2777px;width:190px;height:188px;background:linear-gradient(135deg,#6b3f2a,#3f2418)"></div>
<div class="quote-box" style="left:407px;top:2777px;width:386px;height:188px">
  <span style="width:34px;height:34px;border-radius:50%;background:#b9d4df;border:2px solid #fff;margin-top:24px" role="img" aria-label="Client avatar"></span>
  <p style="font-size:11px;line-height:18.5px;width:320px;margin-top:10px">Lorem ipsum dolor sit amet, consectetur adipiscing elit, sed do eiusmod tempor incididunt ut labore et dolore magna aliqua. Quis ipsum suspendisse ultrices gravida. Risus commodo viverra maecenas accumsan lacus vel facilisis.</p>
  <p style="font-size:11px;font-weight:700;margin-top:8px">JANE ROWE</p>
</div>
<div class="photo" role="img" aria-label="Thoughtful woman resting chin on hand" style="left:799px;top:2777px;width:191px;height:387px;background:linear-gradient(180deg,#8b7a72,#c7b3a7)"></div>
<div class="photo" role="img" aria-label="Group of women of different ages laughing in white shirts" style="left:210px;top:2975px;width:387px;height:189px;background:linear-gradient(135deg,#efeceb,#cfc7c2)"></div>
<div class="photo" role="img" aria-label="Before and after skin comparison" style="left:603px;top:2975px;width:190px;height:189px;background:linear-gradient(90deg,#c49b8a 0 50%,#e5cabd 50% 100%)"></div>
<div class="abs" style="left:697px;top:2975px;width:2px;height:189px;background:#fff"></div>
<div class="btn" style="left:533px;top:3204px;width:135px;height:43px">View All</div>

<!-- FORMS -->
<section class="band" style="top:3315px;height:398px;background:var(--white)"></section>
<div class="abs" style="left:0;top:3315px;width:600px;height:398px;background:var(--grey-panel)"></div>

<h3 class="abs" style="left:210px;top:3368px;font-size:24px;line-height:28px">REFER A FREIND &amp;<br>GET 25% OFF</h3>
<div class="field" style="left:210px;top:3454px;width:291px">Their Email</div>
<div class="field" style="left:210px;top:3495px;width:291px">Their Name</div>
<div class="field" style="left:210px;top:3535px;width:291px">Your Name</div>
<div class="btn" style="left:210px;top:3576px;width:291px;height:30px;font-size:10px">Submit</div>

<h3 class="abs" style="left:696px;top:3368px;font-size:24px">BOOK AN APPOINTMENT</h3>
<p class="abs para" style="left:696px;top:3401px;width:291px;text-align:right;font-size:12px">Lorem ipsum dolor sit amet, consectetur adipiscing elit sed do eiusmod tempor incididunt.</p>
<div class="field" style="left:696px;top:3454px;width:291px">Your Email</div>
<div class="field" style="left:696px;top:3495px;width:291px">Your Name</div>
<div class="field" style="left:696px;top:3535px;width:291px">Number</div>
<div class="btn" style="left:696px;top:3576px;width:291px;height:30px;font-size:10px">Book an Appointment</div>

<!-- FOOTER -->
<footer class="band" style="top:3713px;height:384px;background:var(--ink)">
  <div class="abs" style="left:0;width:1200px;top:40px;display:flex;justify-content:center;align-items:center;gap:12px;color:#fff">
    <span style="width:42px;height:42px;border:1.5px solid #fff;border-radius:50%"></span>
    <div><div style="font-size:28px;line-height:1">Glow Muse</div><div style="font-size:7px;letter-spacing:3px;margin-top:4px">CONCIERGE AESTHETICS</div></div>
  </div>
</footer>
<div class="footer-col" style="left:162px;width:240px;top:3866px"><h4>ADDRESS</h4><p>0000 Linden Blvd #000<br>Maple City, USA 00000</p></div>
<div class="divider" style="left:440px"></div>
<div class="footer-col" style="left:452px;width:300px;top:3866px"><h4>GIVE US A CALL</h4><p style="font-size:22px;letter-spacing:4px;color:#fff;text-decoration:underline;text-underline-offset:5px;line-height:30px">(000) 000-0000</p></div>
<div class="divider" style="left:758px"></div>
<div class="footer-col" style="left:760px;width:266px;top:3866px"><h4>EMAIL</h4><p style="line-height:16px">info@glowmuseaesthetics.com<br>info@glowmuseaesthetics.com</p></div>
<span class="social" style="left:501px"></span>
<span class="social" style="left:558px"></span>
<span class="social" style="left:614px"></span>
<span class="social" style="left:668px"></span>
<div class="abs" style="left:210px;top:4052px;width:780px;height:1px;background:#444"></div>
<div class="abs" style="left:0;width:1200px;top:4067px;text-align:center;font-size:11px;color:#fff">© 2022 <u style="font-weight:700">GLOW MUSE CONCIERGE AESTHETIC</u> All Rights Reserved</div>

</body>
</html>
```